New counselling and hypnotherapy business

I'd like a flyer which is relevant to people who want support and to improve their wellbeing which follows the same theme as my website: http://wrenlowtherapy.sitepailo.com
And emphasise that whatever the area of concern, development or growth and I can tailor my knowledge and skills to help.

I'd like to use the same logo and my emphasis is to draw the audience in...therapy and counselling is for people who are "stuck" and having a difficult time...it can also be useful has a personal development tool.

Hypnotherapy

```html
<!DOCTYPE html>
<html lang="en">
<head>
<meta charset="utf-8">
<title>Wrenlow Counselling &amp; Hypnotherapy – Flyer</title>
<link rel="stylesheet" href="https://fonts.googleapis.com/css2?family=Rosario:wght@400&family=Ubuntu:wght@400;500;700&family=Didact+Gothic&display=swap">
<style>
  :root{
    --plum:#4d2a4f;
    --plum-deep:#3f2142;
    --leaf:#3aa845;
    --ink:#2f2f2f;
    --paper:#ffffff;
    --mist:#f1f1f1;
  }
  *{margin:0;padding:0;box-sizing:border-box}
  html,body{width:884px;height:1200px;overflow:hidden;background:var(--mist)}
  .flyer{position:relative;width:884px;height:1200px;background:linear-gradient(#fff,#f7f7f7);overflow:hidden;font-family:"Didact Gothic",sans-serif;color:var(--ink)}

  .lead-quote{position:absolute;left:55px;top:50px;width:520px;font-family:"Rosario",sans-serif;font-size:22.5px;line-height:29px;color:#444}

  .brand{position:absolute;left:612px;top:92px;width:250px;text-align:center;font-family:"Ubuntu",sans-serif;font-weight:500;color:var(--plum);letter-spacing:1px;text-transform:uppercase}
  .brand .brand-dot{display:block;width:26px;height:26px;border-radius:50%;background:var(--plum);margin:0 auto 12px}
  .brand .brand-name{display:block;font-size:22px;line-height:24px}
  .brand .brand-sub{display:block;font-size:14px;line-height:18px;margin-top:4px}

  .hero{position:absolute;left:0;top:185px;width:884px;height:330px}

  .concerns{position:absolute;left:37px;top:517px;width:810px;height:221px;display:grid;grid-template-columns:389px 417px;grid-template-rows:106px 111px;gap:4px}
  .concern{background:var(--plum);color:#fff;text-align:center;padding-top:13px}
  .concern:nth-child(1){border-top-left-radius:16px}
  .concern:nth-child(2){border-top-right-radius:16px}
  .concern:nth-child(3){border-bottom-left-radius:16px}
  .concern:nth-child(4){border-bottom-right-radius:16px}
  .concern h2{font-family:"Ubuntu",sans-serif;font-weight:500;font-size:17px;margin-bottom:6px}
  .concern p{font-size:11.5px;line-height:14px}
  .concern.spaced p{line-height:17.5px}

  .about-title{position:absolute;left:49px;top:774px;font-family:"Ubuntu",sans-serif;font-weight:500;font-size:23px;color:var(--plum-deep)}
  .portrait{position:absolute;left:683px;top:764px;width:145px;height:203px;border-radius:6px;background:linear-gradient(160deg,#f4f2f0 0%,#e2ddd8 55%,#b56a6a 78%,#5d6f8f 100%)}
  .about{position:absolute;left:49px;top:810px;width:788px;font-size:11.4px;line-height:13.6px}
  .about p{margin-bottom:12px}
  .about p.narrow{width:598px}

  .footer{position:absolute;left:0;bottom:0;width:884px;height:120px}
  .footer svg{position:absolute;left:0;top:0}
  .contact{position:absolute;color:#fff;font-family:"Ubuntu",sans-serif;font-weight:700}
  .address{left:31px;top:1143px;font-size:12.5px;line-height:15px;display:flex;gap:4px}
  .address span{display:block}
  .phone{left:318px;top:1157px;font-size:22px;display:flex;align-items:center;gap:4px}
  .web{left:587px;top:1146px;font-size:12.5px;line-height:17px}
  .web div{display:flex;align-items:center;gap:5px}
  .social{position:absolute;top:1160px;display:flex;gap:6px;left:809px}
  .social span{width:22px;height:22px;border-radius:3px;background:#3f78c7;display:block}
</style>
</head>
<body>
<main class="flyer">

  <p class="lead-quote">Sometimes when I'm in the boat alone, it doesn't feel like I have any oars. ... up out of the fog, I can see your harbour light somewhere out there, guiding me in.</p>

  <div class="brand">
    <span class="brand-dot"></span>
    <span class="brand-name">Wrenlow</span>
    <span class="brand-sub">Counselling &amp; Hypnotherapy</span>
  </div>

  <svg class="hero" viewBox="0 0 884 330" xmlns="http://www.w3.org/2000/svg">
    <defs>
      <linearGradient id="sunset" x1="0" y1="0" x2="0" y2="1">
        <stop offset="0" stop-color="#7d7a84"/>
        <stop offset="0.35" stop-color="#cbbfb3"/>
        <stop offset="0.5" stop-color="#9b948f"/>
        <stop offset="0.75" stop-color="#4a4645"/>
        <stop offset="1" stop-color="#2d2a2a"/>
      </linearGradient>
    </defs>
    <path d="M38 16 Q450 -6 884 28 L884 38 Q450 6 38 16Z" fill="var(--plum)"/>
    <g role="img" aria-label="Family walking hand in hand along a beach at sunset">
      <path d="M0 24 Q450 8 884 52 L884 288 Q450 322 0 268Z" fill="url(#sunset)"/>
    </g>
    <path d="M0 268 Q450 322 884 288 L884 304 Q450 330 0 282Z" fill="var(--plum)"/>
    <path d="M0 286 Q450 335 845 300 Q450 334 0 292Z" fill="var(--plum)"/>
  </svg>

  <section class="concerns">
    <article class="concern">
      <h2>Clarify</h2>
      <p>I want to understand more about my relationship with others.<br>I'm not sure how to cope with my grief and loss.<br>I feel anxious and scared and I'm not sure why.<br>I'm not sure how to relax.</p>
    </article>
    <article class="concern">
      <h2>Growth and development</h2>
      <p>I want to improve my level of confidence and self esteem.<br>I want to personally gain a greater self awareness.<br>I want to improve communication with my manager and my team.<br>I want to move on to something else.</p>
    </article>
    <article class="concern">
      <h2>Explore</h2>
      <p>There's something I want to explore and make sense of.<br>I'm feeling really down, low and depressed and I feel stuck.<br>To me the world just looks like a fog.<br>I'd like to have some support and somebody to listen.<br>I feel overwhelmed.</p>
    </article>
    <article class="concern spaced">
      <h2>Behaviour change</h2>
      <p>I want to stop smoking.<br>I want to feel less anxious.<br>I want to stop harming myself.<br>I want to stop the phobia I have.</p>
    </article>
  </section>

  <h1 class="about-title">Trusted Professional An approach tailored to you</h1>
  <div class="portrait" role="img" aria-label="Portrait of the counsellor seated in a chair, smiling"></div>

  <section class="about">
    <p class="narrow">There are times in all of our lives when we feel we have lost our way, we need a listening ear or we simply want somebody to work together with to help us reach the next step in our journey, whatever that may be. Maybe that sounds like you and you're looking for somebody to help you take that first step or maybe you simply want somebody to share your concerns with and really feel heard.</p>
    <p class="narrow">I am a fully qualified counsellor and I'm able to provide a safe, confidential environment for you to speak, to feel, to be heard and valued as an individual in what can be a scary and challenging world.</p>
    <p class="narrow">I have experience of working with people with a wide range of concerns. Some examples include loss and grief, depression, anxiety, relationships, self-esteem, eating disorders, confidence, general personal development and growth. I find this work really rewarding and it's been a privilege to work with all of these people.</p>
    <p>My main way of working is based on the Transactional Analysis model and I also able to use a wide range of techniques and theories, tailoring my approach to suit you. Some examples include NLP, CBT, EFT, Mindfulness, creative sand-tray.</p>
    <p>In addition to a more typical counselling role, I am able to offer hypnotherapy. I find this works really well in combination with counselling. I am also happy to offer this on its own for specific things such as giving up smoking, phobias, relaxation, confidence and much more.</p>
    <p>I'm happy to support individuals over fourteen years of age and couples on a face-to-face basis for short, medium or long term therapy.</p>
  </section>

  <footer class="footer">
    <svg width="884" height="120" viewBox="0 0 884 120" xmlns="http://www.w3.org/2000/svg">
      <path d="M0 20 Q420 -12 884 62 L884 120 L0 120Z" fill="var(--plum)"/>
      <path d="M0 14 Q420 -18 884 56 L884 64 Q420 -8 0 22Z" fill="var(--leaf)"/>
    </svg>
  </footer>

  <div class="contact address">
    <svg width="11" height="14" viewBox="0 0 11 14"><path d="M5.5 0A5.5 5.5 0 0 0 0 5.5C0 9.5 5.5 14 5.5 14S11 9.5 11 5.5A5.5 5.5 0 0 0 5.5 0Zm0 7.6a2.1 2.1 0 1 1 0-4.2 2.1 2.1 0 0 1 0 4.2Z" fill="#fff"/></svg>
    <div><span>Wrenlow Counselling &amp; Hypnotherapy,</span><span>12B, Harbour Lane, Eastmere</span><span>West Downs WD4 7QR</span></div>
  </div>

  <div class="contact phone">
    <svg width="18" height="18" viewBox="0 0 18 18"><circle cx="9" cy="9" r="8" fill="none" stroke="#fff" stroke-width="1.4"/><path d="M6 5l2 2-1 1c.6 1.3 1.6 2.3 3 3l1-1 2 2-1.3 1.3C8.5 12.8 5.2 9.5 4.7 6.3Z" fill="#fff"/></svg>
    07700 900418
  </div>

  <div class="contact web">
    <div><svg width="13" height="10" viewBox="0 0 13 10"><rect x=".6" y=".6" width="11.8" height="8.8" fill="none" stroke="#fff" stroke-width="1.2"/><path d="M.6.6l5.9 5 5.9-5" fill="none" stroke="#fff" stroke-width="1.2"/></svg>wrenlowtherapy@mailpost.com</div>
    <div><svg width="12" height="12" viewBox="0 0 12 12"><circle cx="6" cy="6" r="5.3" fill="none" stroke="#fff" stroke-width="1.2"/><path d="M.7 6h10.6M6 .7c-3 3-3 7.6 0 10.6M6 .7c3 3 3 7.6 0 10.6" fill="none" stroke="#fff" stroke-width="1"/></svg>wrenlowtherapy.sitepailo.com</div>
  </div>

  <div class="social"><span></span><span></span></div>

</main>
</body>
</html>
```